Business card for different employees

A professional new updated design incorporating our current business's color themes and styles such as our on-site service trucks decals included in pictures attached. Our current business card is very simple and not professionally designed. We are a small family business but want a professional corporate look.

Target Market(s)

Cards to be handed out to new customers , corperate meetings. For our on site service operators.

Industry/Entity Type

Hydraulic

Contact Information for Business Card

Address, website, phone number, email, logo.
slogan - "Industry chosen hose and fittings provider".
24/7 on-site service , supply and hose management
Experienced , indpendant , family owned

Font styles to use
Sans Serif

Requirements
Must have
• Easily editable so that I can add different names and different roles for employees etc.
Nice to have
• Freedom with colour doesn't necessarily have to be blue but that is our company colour theme with trucks and logo so makes sense for the card to have blue like the trucks.

```html
<!DOCTYPE html>
<html lang="en">
<head>
<meta charset="utf-8">
<title>Meridian Hose and Fittings – Business Card</title>
<link rel="stylesheet" href="https://fonts.googleapis.com/css2?family=Arimo:ital,wght@0,400;0,700;1,700&display=swap">
<style>
  :root {
    --brand-blue: #0a56b0;
    --brand-blue-light: #5b8fcb;
    --ink: #1c1c1c;
    --paper: #ffffff;
    --backdrop: #e9e7e3;
    --card-w: 540px;
    --card-h: 310px;
  }
  * { box-sizing: border-box; margin: 0; padding: 0; }
  html, body { width: 1200px; height: 892px; overflow: hidden; }
  body {
    background: var(--backdrop);
    font-family: "Arimo", Arial, sans-serif;
    color: var(--ink);
    display: flex;
    align-items: center;
    justify-content: center;
    gap: 60px;
  }
  .card {
    width: var(--card-w);
    height: var(--card-h);
    background: var(--paper);
    position: relative;
    overflow: hidden;
    box-shadow: 0 6px 18px rgba(0,0,0,.18);
  }

  /* Brand lockup */
  .brand { display: flex; align-items: center; gap: 10px; }
  .brand-dot {
    width: 30px; height: 30px; border-radius: 50%;
    background: var(--ink); flex: none;
  }
  .brand-name {
    font-weight: 700; color: var(--ink);
    line-height: 1.05; text-transform: uppercase;
  }
  .brand-name .word { display: block; font-size: 26px; letter-spacing: 1px; }
  .brand-name .sub { display: block; font-size: 10px; letter-spacing: 2.5px; }

  /* Front */
  .card-front .pattern-field {
    position: absolute; inset: 0 0 56px 0;
    background: linear-gradient(135deg, #dfe9f6, #9fbde3 50%, #dfe9f6);
  }
  .card-front .brand-plate {
    position: absolute; left: 50%; top: 122px; transform: translateX(-50%);
    background: var(--paper); padding: 10px 16px;
  }
  .card-front .slogan-band {
    position: absolute; left: 0; right: 0; bottom: 0; height: 56px;
    background: var(--brand-blue); color: var(--paper);
    display: flex; align-items: center; justify-content: center;
    font-weight: 700; font-size: 16px; letter-spacing: .6px; text-transform: uppercase;
  }

  /* Back */
  .card-back { display: flex; }
  .contact-side {
    width: 46%; padding: 22px 20px 18px;
    display: flex; flex-direction: column; align-items: center;
  }
  .contact-side .brand { align-self: flex-start; }
  .contact-list { list-style: none; text-align: center; margin-top: 18px; font-size: 14px; line-height: 1.25; }
  .contact-list li { display: flex; flex-direction: column; align-items: center; margin-bottom: 6px; }
  .contact-list svg { width: 12px; height: 12px; margin-bottom: 2px; fill: none; stroke: var(--brand-blue); stroke-width: 2; }
  .service-lines {
    margin-top: auto; text-align: center;
    color: var(--brand-blue); font-weight: 700; font-style: italic; font-size: 13px; line-height: 1.35;
  }
  .values-side {
    flex: 1; background: var(--brand-blue); color: var(--paper);
    display: flex; flex-direction: column; align-items: center; justify-content: center;
    position: relative;
  }
  .values {
    list-style: none; text-align: center;
    font-weight: 700; font-size: 19px; line-height: 1.25;
  }
  .website {
    position: absolute; bottom: 18px; left: 0; right: 0; text-align: center;
    font-size: 13px; letter-spacing: .3px;
  }
</style>
</head>
<body>

  <section class="card card-front" aria-label="Business card front">
    <div class="pattern-field" role="img" aria-label="Repeating blue and white circular brand pattern"></div>
    <div class="brand brand-plate">
      <span class="brand-dot"></span>
      <span class="brand-name"><span class="word">Meridian</span><span class="sub">Hose and Fittings</span></span>
    </div>
    <div class="slogan-band">Industry chosen hose and fittings provider</div>
  </section>

  <section class="card card-back" aria-label="Business card back">
    <div class="contact-side">
      <div class="brand">
        <span class="brand-dot"></span>
        <span class="brand-name"><span class="word">Meridian</span><span class="sub">Hose and Fittings</span></span>
      </div>
      <ul class="contact-list">
        <li>
          <svg viewBox="0 0 24 24" aria-hidden="true"><path d="M5 3h4l2 5-3 2a12 12 0 0 0 6 6l2-3 5 2v4a2 2 0 0 1-2 2A18 18 0 0 1 3 5a2 2 0 0 1 2-2z"/></svg>
          <span class="phone">0400 555 123</span>
        </li>
        <li>
          <svg viewBox="0 0 24 24" aria-hidden="true"><rect x="2" y="5" width="20" height="14"/><path d="M2 5l10 8 10-8"/></svg>
          <span class="email">name@example.com</span>
        </li>
        <li>
          <svg viewBox="0 0 24 24" aria-hidden="true"><path d="M12 22s7-7 7-12a7 7 0 0 0-14 0c0 5 7 12 7 12z"/><circle cx="12" cy="10" r="2.5"/></svg>
          <span class="address">your address<br>here</span>
        </li>
      </ul>
      <p class="service-lines">24/7 On-site service<br>Supply and hose management</p>
    </div>
    <div class="values-side">
      <ul class="values">
        <li>Experienced</li>
        <li>Independent</li>
        <li>Family owned</li>
      </ul>
      <p class="website">www.meridianhose.com.au</p>
    </div>
  </section>

</body>
</html>
```